New Website for IT Services Business

We need an uncoded web design for a new company based in Australia called "Falcon IT". We offer specialised point of sale (POS) support to the hospitality industry. We already support hundreds of cafes and restaurants. We are also about to launch and promote a range of new services with the offering of General IT Support being the most important. Other additional services to be offered are Falcon Vault Storage, reselling and supporting Corvel Shieldware and Trelmo Suite.

We have a logo design and our colour scheme is based on the logo with the addition of charcoal grey (see attached logos). We want the pages to reflect precision and efficiency with sharp characteristics. It must be professional but playful/fun elements are encouraged.

Our target audience is restaurant and cafe owners who are interested in finding high quality POS and IT support for their business.

The main call to action on the home page should be either 'Let's Meet For Coffee!' or 'Find out more (by completing a form)'. If you are unsure about what the general text should say then you can use 'Lorem Ipsum' where required.

The site must be viewable at different resolutions and on smart phones and tablets.

The website structure will be quite simple. We require:
- one impressive landing page. Visitors will quickly determine our services and that we provide a very high level of service while also offering value for money. Obviously a clear list of links (however/wherever you like) to the other pages.
- Simple pages with a similar layout for the following:
- Services - "POS & IT Support for the Hospitality Industry" being the main one. With complementary services also listed. Another call to action on this page with the option of 'Let's Meet For Coffee' or a "More information/Pricing" form to be completed by the visitor.
- Products - will be a small online storefront for a few simple products.
- About - Business background. 2x Directors with a photo and brief Bio.
- Downloads - A list of free files to download. Includes remote access client software.
- Contact Us - Mailing address, Email addresses and Support phone number.

Please feel free to ask any questions about the design. I will assist as much as possible.

Thank you for viewing. We promise to give constructive feedback to every person who submits a design. Thank you so much.

Target Market(s)

Restaurant and Cafe owners.

Industry/Entity Type

Hospitality

Requirements
Must have
• - Viewable on different resolutions and on smart phones and tablets.
- Clear call to action of EITHER 'Let's Meet For Coffee' or a "More information/Pricing" form to be completed by the visitor.

```html
<!DOCTYPE html>
<html lang="en">
<head>
<meta charset="utf-8">
<title>Falcon IT – Home</title>
<link rel="stylesheet" href="https://fonts.googleapis.com/css2?family=Federo&family=Noto+Sans:wght@400;700&display=swap">
<style>
  :root {
    --brand-red: #c41e2f;
    --brand-red-glow: #e2303e;
    --charcoal: #2b2b2d;
    --tab-grey: #cccccc;
    --field-grey: #c8c8c8;
    --field-text: #555555;
    --photo-dark: #3a2d24;
    --photo-warm: #8a6a4c;
    --white: #ffffff;
  }
  * { box-sizing: border-box; margin: 0; padding: 0; }
  html, body { width: 1200px; height: 918px; overflow: hidden; background: var(--white); }
  body { position: relative; font-family: "Noto Sans", Verdana, sans-serif; }

  .site-header { position: absolute; left: 0; top: 0; width: 1200px; height: 165px; }
  .brand { position: absolute; left: 366px; top: 22px; display: flex; align-items: center; gap: 22px; }
  .brand-mark { width: 108px; height: 108px; border-radius: 50%; background: var(--brand-red); }
  .brand-name { font-family: "Noto Sans", Verdana, sans-serif; font-weight: 700; font-size: 74px; color: var(--charcoal); line-height: 1; }

  .nav-rule { position: absolute; left: 0; top: 164px; width: 1200px; height: 10px; background: var(--brand-red); }
  .main-nav { position: absolute; left: 0; top: 174px; width: 1200px; height: 55px; }
  .nav-tab {
    position: absolute; top: 0; height: 54px; width: 180px;
    background: var(--tab-grey); color: var(--brand-red);
    border-radius: 0 0 12px 12px;
    font-family: "Federo", Georgia, serif; font-size: 31px;
    display: flex; align-items: center; justify-content: center;
    text-decoration: none;
  }
  .nav-tab.is-active { background: var(--brand-red); color: #f2e4e4; }

  .hero-title {
    position: absolute; left: 567px; top: 306px;
    font-size: 43px; font-weight: 400; color: var(--brand-red); letter-spacing: 0.5px;
  }
  .venue-photo {
    position: absolute; left: 79px; top: 397px; width: 503px; height: 336px;
    background: linear-gradient(160deg, var(--photo-warm) 0%, var(--photo-dark) 45%, #1d1814 75%, #6f5a48 100%);
  }

  .enquiry { position: absolute; left: 749px; top: 440px; width: 320px; }
  .enquiry-title { font-size: 28px; font-weight: 400; color: var(--brand-red); margin-bottom: 18px; }
  .field {
    display: block; width: 306px; background: var(--field-grey); border: none;
    box-shadow: 4px 4px 4px rgba(0,0,0,0.55);
    font-family: "Noto Sans", Verdana, sans-serif; font-size: 14px; color: var(--field-text);
    padding: 0 4px; margin-bottom: 7px; resize: none;
  }
  .field-line { height: 37px; line-height: 1; padding-top: 2px; }
  .field-area { height: 104px; padding-top: 2px; }
  .send-btn {
    width: 87px; height: 28px; background: var(--field-grey); border: none;
    box-shadow: 4px 4px 4px rgba(0,0,0,0.55);
    font-family: "Noto Sans", Verdana, sans-serif; font-size: 19px; color: var(--field-text);
  }

  .site-footer { position: absolute; left: 0; top: 826px; width: 1200px; height: 92px; background: var(--brand-red); }
  .footer-brand {
    position: absolute; left: 0; top: 0; width: 159px; height: 92px;
    background: radial-gradient(circle at 50% 50%, var(--brand-red-glow) 0%, var(--brand-red) 70%);
    display: flex; align-items: center; justify-content: center; gap: 8px;
  }
  .footer-dot { width: 24px; height: 24px; border-radius: 50%; background: var(--white); }
  .footer-name { color: var(--white); font-size: 15px; font-weight: 700; }
  .footer-link {
    position: absolute; top: 24px; height: 42px; padding-left: 8px;
    border-left: 3px solid #6e6e6e; color: var(--white);
    font-family: "Federo", Georgia, serif; font-size: 18px;
    display: flex; align-items: center; text-decoration: none;
  }
</style>
</head>
<body>
  <header class="site-header">
    <div class="brand">
      <span class="brand-mark"></span>
      <span class="brand-name">Falcon IT</span>
    </div>
  </header>
  <div class="nav-rule"></div>
  <nav class="main-nav">
    <a class="nav-tab is-active" style="left:32px;width:177px" href="#">Home</a>
    <a class="nav-tab" style="left:220px" href="#">Services</a>
    <a class="nav-tab" style="left:409px;width:179px" href="#">Produts</a>
    <a class="nav-tab" style="left:600px" href="#">About</a>
    <a class="nav-tab" style="left:792px;width:182px" href="#">Downloads</a>
    <a class="nav-tab" style="left:982px;width:184px" href="#">Contact us</a>
  </nav>

  <main>
    <h1 class="hero-title">'Let's Meet For Coffee!'</h1>
    <div class="venue-photo" role="img" aria-label="Photo of a modern restaurant lounge with a suspended fireplace, white seating and warm wood beams"></div>
    <form class="enquiry">
      <h2 class="enquiry-title">Find out more</h2>
      <input class="field field-line" type="email" placeholder="email">
      <input class="field field-line" type="text" placeholder="subject">
      <textarea class="field field-area" placeholder="message"></textarea>
      <button class="send-btn" type="button">Send</button>
    </form>
  </main>

  <footer class="site-footer">
    <div class="footer-brand">
      <span class="footer-dot"></span>
      <span class="footer-name">Falcon IT</span>
    </div>
    <a class="footer-link" style="left:590px" href="#">Quick Link</a>
    <a class="footer-link" style="left:739px" href="#">Our Team</a>
    <a class="footer-link" style="left:888px" href="#">Get Help</a>
    <a class="footer-link" style="left:1048px" href="#">Privacy Note</a>
  </footer>
</body>
</html>
```